Fancy looking Inspection Postcard

Postcard needed for customers to inspect their product once it is delivered. We'll be giving them the steps for inspecting their product and to contact us if any issues arise. Would like to see something that sticks out but uses our company's colors. Would like to see creativity. Possibly utilizing the diamond steel background like we have in our logo.

Target Market(s)

Customers of our manufacturing shop

Industry/Entity Type

Manufacturing - metal wall art, custom products

Requirements
Must have
• our colors and logo
Nice to have
• get creative. i like creativity

```html
<!DOCTYPE html>
<html lang="en">
<head>
<meta charset="utf-8">
<title>Cedar Ridge Fabrication – Inspection Postcard</title>
<link rel="stylesheet" href="https://fonts.googleapis.com/css2?family=Roboto+Condensed:wght@400;500;700&display=swap">
<style>
  :root {
    --green: #76a043;
    --green-deep: #5f8a34;
    --dark: #333333;
    --ink: #111111;
    --light: #e8e8e8;
    --yellow: #e8e21c;
    --white: #ffffff;
    --rule: #a6a6a6;
    --stage-a: #4f4f4f;
    --stage-b: #7d7d7d;
  }
  html, body {
    margin: 0;
    padding: 0;
    width: 835px;
    height: 1200px;
    overflow: hidden;
    background: var(--white);
  }
  .postcard-sheet {
    display: block;
    width: 835px;
    height: 1200px;
    font-family: "Roboto Condensed", "Arial Narrow", sans-serif;
  }
  .headline { font-weight: 500; fill: var(--white); font-size: 44px; }
  .contact-dark { font-weight: 500; fill: var(--ink); font-size: 44px; }
  .call-line { font-weight: 500; fill: var(--white); font-size: 46px; }
  .text-label { font-weight: 500; fill: var(--white); font-size: 39px; }
  .text-number { font-weight: 500; fill: var(--white); font-size: 66px; }
  .area-code { fill: var(--green); }
  .web-address { font-weight: 500; fill: var(--white); font-size: 35px; }
  .brand-name { font-weight: 700; fill: var(--ink); font-size: 26px; letter-spacing: 0.5px; }
  .brand-name-small { font-weight: 700; fill: var(--ink); font-size: 19px; }
  .step-title { font-weight: 500; fill: var(--white); font-size: 23px; }
  .step-item { font-weight: 500; fill: var(--white); font-size: 23px; }
  .bullet { fill: var(--yellow); }
  .back-contact { font-weight: 500; fill: var(--ink); font-size: 33px; }
  .back-call { font-weight: 500; fill: var(--green); font-size: 33px; }
</style>
</head>
<body>
<svg class="postcard-sheet" viewBox="0 0 1217 1750" width="835" height="1200" xmlns="http://www.w3.org/2000/svg">
  <defs>
    <linearGradient id="stage" x1="0" y1="0" x2="1" y2="1">
      <stop offset="0" stop-color="var(--stage-b)"/>
      <stop offset="1" stop-color="var(--stage-a)"/>
    </linearGradient>
    <linearGradient id="sky" x1="0" y1="0" x2="0.3" y2="1">
      <stop offset="0" stop-color="#4a8fd6"/>
      <stop offset="0.6" stop-color="#a9c9ea"/>
      <stop offset="1" stop-color="#7f8b98"/>
    </linearGradient>
    <linearGradient id="plate" x1="0" y1="0" x2="1" y2="1">
      <stop offset="0" stop-color="#f4f4f4"/>
      <stop offset="1" stop-color="#e6e6e6"/>
    </linearGradient>
    <linearGradient id="green-photo" x1="0" y1="0" x2="1" y2="1">
      <stop offset="0" stop-color="#6f9a3f"/>
      <stop offset="0.6" stop-color="#7aa54a"/>
      <stop offset="1" stop-color="#5f8a34"/>
    </linearGradient>
  </defs>

  <rect class="backdrop" x="16" y="16" width="1186" height="1716" fill="url(#stage)"/>

  <!-- FRONT SIDE -->
  <g class="card-front">
    <rect x="63" y="82" width="1079" height="751" fill="var(--white)"/>
    <rect class="plate-band" x="63" y="82" width="1079" height="221" fill="url(#plate)" role="img" aria-label="Diamond steel plate texture"/>
    <polygon class="url-tab" points="755,230 790,158 1142,158 1142,230" fill="var(--green)"/>
    <text class="web-address" x="957" y="212" text-anchor="middle">www.cedarridgefab.com</text>

    <polygon class="hero-photo" points="712,231 1142,231 1142,660 470,660" fill="url(#sky)" role="img" aria-label="Photo of a steel building frame against a blue sky"/>
    <polygon class="green-panel" points="63,303 575,303 620,231 700,231 500,573 63,573" fill="var(--green)"/>
    <polygon class="email-panel" points="63,573 495,573 570,703 63,703" fill="var(--light)"/>
    <polygon class="dark-panel" points="63,703 570,703 630,660 1142,660 1142,833 535,833 63,833" fill="var(--dark)"/>

    <g class="brand-mark">
      <circle cx="140" cy="205" r="34" fill="var(--dark)"/>
      <text class="brand-name" x="186" y="198">CEDAR RIDGE</text>
      <text class="brand-name" x="186" y="228">FABRICATION</text>
    </g>

    <text class="headline" x="103" y="399">Did we do a good job?</text>
    <rect class="headline-rule" x="103" y="422" width="420" height="3" fill="var(--yellow)"/>
    <text class="headline" x="103" y="477">If you think so leave us</text>
    <text class="headline" x="103" y="534">a review on ReviewHub?</text>

    <text class="contact-dark" x="103" y="625">Please let us know</text>
    <text class="contact-dark" x="103" y="682">info@cedarridgefab.com</text>

    <text class="call-line" x="103" y="775">CALL US 555-318-4420</text>

    <text class="text-label" x="862" y="721" text-anchor="middle">SHOOT US A TEXT</text>
    <text class="text-number" x="862" y="797" text-anchor="middle"><tspan class="area-code">(555)</tspan> 207-6193</text>
  </g>

  <!-- BACK SIDE -->
  <g class="card-back">
    <rect x="76" y="880" width="1053" height="752" fill="var(--white)"/>
    <polygon class="steps-panel" points="76,880 725,880 530,1418 76,1418" fill="url(#green-photo)" role="img" aria-label="Green-tinted photo of a steel building frame"/>
    <polygon class="edge-stripe" points="725,880 737,880 578,1318 566,1318" fill="var(--dark)"/>
    <polygon class="dark-panel" points="76,1418 530,1418 560,1340 695,1632 76,1632" fill="var(--dark)"/>

    <g class="inspection-steps">
      <text class="step-title" x="122" y="960">Step 1.  Inspect general shape</text>
      <circle class="bullet" cx="126" cy="981" r="5"/>
      <text class="step-item" x="136" y="989">Is it what you expected?</text>
      <circle class="bullet" cx="126" cy="1011" r="5"/>
      <text class="step-item" x="136" y="1019">Is it bent, disoriented?</text>

      <text class="step-title" x="122" y="1077">Step 2.  Inspect the welds if there are any</text>
      <circle class="bullet" cx="126" cy="1099" r="5"/>
      <text class="step-item" x="136" y="1107">Do they look clean?</text>
      <circle class="bullet" cx="126" cy="1128" r="5"/>
      <text class="step-item" x="136" y="1136">Are there any gaps?</text>

      <text class="step-title" x="122" y="1194">Step 3.  Inspect the finish</text>
      <circle class="bullet" cx="126" cy="1216" r="5"/>
      <text class="step-item" x="136" y="1224">Are there any areas not finished?</text>
      <circle class="bullet" cx="126" cy="1245" r="5"/>
      <text class="step-item" x="136" y="1253">Are the colors what you expected?</text>

      <text class="step-title" x="122" y="1312">Step 4.  Check for functionality</text>
      <circle class="bullet" cx="126" cy="1333" r="5"/>
      <text class="step-item" x="136" y="1341">Does it work the way you want it to</text>
      <circle class="bullet" cx="126" cy="1362" r="5"/>
      <text class="step-item" x="136" y="1370">Is it what you expected?</text>
    </g>

    <text class="text-label" x="327" y="1512" text-anchor="middle">SHOOT US A TEXT</text>
    <text class="text-number" x="327" y="1587" text-anchor="middle"><tspan class="area-code">(555)</tspan> 207-6193</text>

    <g class="brand-mark">
      <circle cx="837" cy="985" r="30" fill="var(--dark)"/>
      <text class="brand-name-small" x="837" y="1045" text-anchor="middle">CEDAR RIDGE</text>
      <text class="brand-name-small" x="837" y="1069" text-anchor="middle">FABRICATION</text>
    </g>

    <rect class="stamp-box" x="938" y="945" width="143" height="142" fill="none" stroke="var(--rule)" stroke-width="2"/>

    <g class="address-lines" stroke="var(--rule)" stroke-width="3">
      <line x1="761" y1="1279" x2="1080" y2="1279"/>
      <line x1="761" y1="1360" x2="1080" y2="1360"/>
      <line x1="761" y1="1426" x2="1080" y2="1426"/>
    </g>

    <text class="back-contact" x="1080" y="1512" text-anchor="end">Please let us know</text>
    <text class="back-contact" x="1080" y="1554" text-anchor="end">info@cedarridgefab.com</text>
    <text class="back-call" x="1080" y="1597" text-anchor="end">CALL US 555-318-4420</text>
  </g>
</svg>
</body>
</html>
```